Paperlantern.com.au - Quivora Australia - Uncoded PSD only

We need a web design for a virtual assistant company based in Sydney Australia called "Paperlantern". We provide virtual assistance and unlimited admin tasks to small business owners for a monthly fee. We would like to see designs that are not too different to www.quivora.com. Words to describe the design and feel of this website are sleek and professional. We want to use bright inviting colours for the call to action buttons and a professional business focused background.

Target Market(s)

business executives, business owners, small business owners, those professionals who lack time.

Industry/Entity Type

Business Consultant

Number of Pages Required

3 page

Font styles to use
Sans Serif

Colors
5e5e5e
1b1b1b
3176b5
33b8a4

Requirements
Must have
• Call to action buttons, sleek business feel think vantok.io and quivora.com
Nice to have
• Bold back ground colours, bright call to action buttons
Should not have
• too much white

```html
<!DOCTYPE html>
<html lang="en">
<head>
<meta charset="utf-8">
<title>Paperlantern – Work | Life Balanced</title>
<link href="https://fonts.googleapis.com/css2?family=Lato:wght@300;400;700;900&display=swap" rel="stylesheet">
<style>
:root{
  --blue:#3176b5;
  --blue-dark:#27649c;
  --teal:#33b8a4;
  --ink:#1b1b1b;
  --grey:#5e5e5e;
  --paper:#ffffff;
  --mist:#eef4f7;
  --slate:#3d4147;
  --footer:#2a2d31;
  --footer-deep:#1f2124;
}
*{margin:0;padding:0;box-sizing:border-box}
html,body{width:1200px;height:3004px;overflow:hidden}
body{font-family:'Lato',Arial,sans-serif;color:var(--grey);background:var(--paper)}
section,header,footer{position:relative;width:1200px;overflow:hidden}
.btn{display:inline-block;font-weight:700;font-size:13px;letter-spacing:1px;text-transform:uppercase;color:#fff;padding:13px 30px;border-radius:3px}
.btn-teal{background:var(--teal)}
.btn-blue{background:var(--blue)}
.btn-ghost{border:1px solid rgba(255,255,255,.8)}

/* hero */
.hero{height:560px;color:#fff}
.hero-photo{position:absolute;inset:0;background:linear-gradient(180deg,#6d6a6e 0%,#8a7a72 40%,#4b4a50 80%,#2a2b2f 100%)}
.hero-shade{position:absolute;inset:0;background:linear-gradient(180deg,rgba(20,25,35,.35),rgba(20,25,35,.2) 60%,rgba(10,12,16,.75))}
.topbar{position:absolute;top:0;left:0;right:0;height:34px;display:flex;align-items:center;padding:0 120px;font-size:12px}
.brand{font-weight:700;color:var(--teal);font-size:14px}
.topbar nav{margin-left:60px;display:flex;gap:28px}
.topbar .phone{margin-left:auto;margin-right:30px}
.topbar .btn{padding:6px 18px;font-size:10px}
.hero-copy{position:absolute;top:120px;left:0;right:0;text-align:center}
.hero-copy h1{font-weight:300;font-size:46px;letter-spacing:2px}
.hero-copy h1 .bar{color:var(--teal);margin:0 10px}
.hero-copy h2{font-weight:300;font-size:34px;letter-spacing:14px;text-transform:uppercase;color:var(--teal);margin-top:8px}
.hero-copy p{font-size:17px;line-height:1.5;margin:26px auto 0;width:460px}
.logo-strip{position:absolute;bottom:0;left:0;right:0;height:62px;background:rgba(10,12,16,.55);display:flex;align-items:center;justify-content:center;gap:58px}
.partner{display:flex;align-items:center;gap:8px;font-weight:700;font-size:15px;color:#fff;text-transform:uppercase;letter-spacing:1px}
.partner i{width:14px;height:14px;background:#fff;display:block}

/* secret weapon */
.weapon{height:500px;background:linear-gradient(90deg,#fff 45%,var(--mist))}
.weapon-copy{position:absolute;left:96px;top:70px;width:470px}
.weapon-copy h2{font-size:26px;font-weight:700;color:var(--ink);line-height:1.3}
.weapon-copy h2 em{font-style:normal;color:var(--teal)}
.weapon-copy p{font-size:12.5px;line-height:1.7;margin-top:26px}
.weapon-copy .lead{color:var(--blue);font-weight:700;font-size:16px;margin-top:22px}
.weapon-copy .btn{margin-top:28px}
.weapon-photo{position:absolute;right:0;top:0;width:620px;height:500px;background:linear-gradient(135deg,#e6edf1,#c9d3d9 50%,#d9c3b2)}

/* testimonials */
.words{height:300px;background:var(--blue);color:#fff;text-align:center}
.words h2{padding-top:30px;font-size:26px;font-weight:300;line-height:1.3}
.words h2 b{font-weight:700}
.quote{position:absolute;width:290px;background:#fff;color:var(--grey);font-size:11px;line-height:1.6;text-align:left;padding:16px 20px;border-radius:3px}
.quote.left{left:320px;top:124px}
.quote.right{left:640px;top:150px}
.avatar{position:absolute;width:40px;height:40px;border-radius:50%;background:linear-gradient(135deg,#d3b8a4,#8d6e5b)}
.caption{position:absolute;font-size:10px;color:#fff;width:120px;text-align:center}
.arrow{position:absolute;top:140px}

/* team */
.team{height:520px}
.team-photo{position:absolute;inset:0;background:linear-gradient(90deg,#5b4c45,#a08c80 30%,#7a6a62 55%,#b09a8e 75%,#4f423c)}
.team-card{position:absolute;left:340px;top:120px;width:520px;height:260px;background:rgba(255,255,255,.94);text-align:center;padding-top:26px}
.team-card h2{font-size:24px;color:var(--ink);font-weight:700;line-height:1.3}
.team-card h2 em{font-style:normal;color:var(--teal)}
.team-card p{font-size:11.5px;line-height:1.6;width:420px;margin:14px auto 0}
.team-card .lead{color:var(--blue);font-size:15px;margin-top:12px}
.team-card .btn{margin-top:18px;padding:10px 24px}

/* fraction */
.fraction{height:200px;background:var(--teal);color:#fff}
.fraction h2{position:absolute;left:220px;top:44px;width:540px;font-size:27px;font-weight:300;line-height:1.3}
.fraction p{position:absolute;left:220px;top:132px;width:520px;font-size:11px;line-height:1.6;opacity:.9}
.fraction .btn{position:absolute;left:780px;top:80px}

/* to-do */
.todo{height:380px;background:var(--mist)}
.todo-photo{position:absolute;left:0;top:0;width:400px;height:380px;background:linear-gradient(160deg,#e9eef1,#c7a893 45%,#6b4a3b)}
.todo-copy{position:absolute;left:490px;top:60px;width:420px}
.todo-copy h2{font-size:28px;font-weight:400;color:var(--ink);line-height:1.3}
.todo-copy h2 em{font-style:normal;color:var(--blue)}
.todo-copy p{font-size:11.5px;line-height:1.6;margin-top:16px}
.todo-copy .btn{margin-top:22px;padding:11px 22px}

/* started */
.started{height:220px;background:var(--slate);text-align:center;color:#fff}
.started h2{padding-top:38px;font-size:26px;font-weight:300;line-height:1.3;color:var(--teal)}
.started h2 b{color:#7fb9e8;font-weight:400}
.started p{font-size:11px;line-height:1.6;width:520px;margin:14px auto 0;color:#ccc}
.started .btn{margin-top:18px;padding:10px 26px}

/* footer */
.footer{height:200px;background:var(--footer);color:#aaa;font-size:11px;line-height:1.8}
.fcol{position:absolute;top:44px}
.fcol h4{color:var(--teal);font-size:11px;text-transform:uppercase;letter-spacing:1px;margin-bottom:6px}
.fcontact{position:absolute;left:820px;top:44px}
.fcontact div{display:flex;align-items:center;gap:10px;margin-bottom:14px}
.touch{height:72px;background:var(--blue);color:#fff;display:flex;align-items:center;padding-left:240px}
.touch h3{font-weight:400;font-size:24px;letter-spacing:1px;text-transform:uppercase}
.touch .contact{margin-left:30px;display:flex;align-items:center;gap:10px;background:var(--blue-dark);padding:0 26px;height:72px;font-weight:700;font-size:14px;text-transform:uppercase}
.socials{margin-left:50px;display:flex;gap:6px}
.socials i{width:34px;height:34px;display:block;border-radius:2px}
.legal{height:52px;background:var(--footer-deep);color:#888;font-size:10px;padding:20px 0 0 240px}
</style>
</head>
<body>

<header class="hero">
  <div class="hero-photo" role="img" aria-label="Group photo of smiling business professionals"></div>
  <div class="hero-shade"></div>
  <div class="topbar">
    <span class="brand">Paperlantern</span>
    <nav><span>How it works</span><span>Pricing</span><span>About us</span></nav>
    <span class="phone">+61 (02) 5550 1842</span>
    <span class="btn btn-teal">Get started</span>
  </div>
  <div class="hero-copy">
    <h1>Work<span class="bar">|</span>Life</h1>
    <h2>Balanced</h2>
    <p>Dedicated Virtual Assistants for Small Business Owners, Entrepreneurs and Professionals</p>
  </div>
  <div class="logo-strip">
    <span class="partner"><i></i>Newsline</span>
    <span class="partner"><i></i>Terra Atlas</span>
    <span class="partner"><i></i>Swiftpost</span>
    <span class="partner"><i></i>Corvane</span>
    <span class="partner"><i></i>Tallwick</span>
    <span class="partner"><i></i>Lumora</span>
  </div>
</header>

<section class="weapon">
  <div class="weapon-copy">
    <h2>We are the <em>secret weapon</em> of successful people, not just in work, but in life</h2>
    <p>Our virtual assistants take care of the admin, the inbox, the bookings and the endless small tasks, so you can spend your time on the work that grows your business and the people who matter most.</p>
    <p class="lead">Still Not Sure? Cheers! Travel? Booked</p>
    <span class="btn btn-teal">Learn more</span>
  </div>
  <div class="weapon-photo" role="img" aria-label="Smiling businesswoman working at a laptop"></div>
</section>

<section class="words">
  <h2>Words from happy clients.<br><b>Don't just take our word for it.</b></h2>
  <svg class="arrow" style="left:220px" width="14" height="24" viewBox="0 0 14 24"><path d="M12 2 2 12l10 10" fill="none" stroke="#fff" stroke-width="2"/></svg>
  <svg class="arrow" style="left:966px" width="14" height="24" viewBox="0 0 14 24"><path d="M2 2l10 10L2 22" fill="none" stroke="#fff" stroke-width="2"/></svg>
  <div class="quote left">My assistant handles my inbox and calendar every day. I finally have evenings back with my family again.</div>
  <div class="avatar" style="left:410px;top:220px" role="img" aria-label="Client portrait"></div>
  <span class="caption" style="left:370px;top:266px">Sarah Whitfield</span>
  <div class="quote right">Every booking, invoice and follow-up is done before I ask. It is like having a full team behind me.</div>
  <div class="avatar" style="left:765px;top:236px" role="img" aria-label="Client portrait"></div>
  <span class="caption" style="left:725px;top:282px">James Cortland</span>
</section>

<section class="team">
  <div class="team-photo" role="img" aria-label="Grid of portrait photos of the assistant team"></div>
  <div class="team-card">
    <h2>Meet our Administers.<br>These people are <em>superhuman</em></h2>
    <p>Every assistant is hand picked, trained and based in Australia, ready to take on your admin, research and scheduling tasks with care.</p>
    <p class="lead">Smart, reliable, dedicated virtual assistants</p>
    <span class="btn btn-blue">Meet the team</span>
  </div>
</section>

<section class="fraction">
  <h2>Get a dedicated Virtual Assistant for just a fraction of what an in-office EA would cost!</h2>
  <p>No recruiting, no office space and no payroll. Just one simple monthly fee for unlimited admin tasks.</p>
  <span class="btn btn-ghost">See our pricing</span>
</section>

<section class="todo">
  <div class="todo-photo" role="img" aria-label="Smiling couple standing together"></div>
  <div class="todo-copy">
    <h2>Give us your <em>to-do list</em> so you can get on with your love-to-do list.</h2>
    <p>Hand over the tasks that drain your week and spend more time doing what you love, with the people you love.</p>
    <span class="btn btn-teal">Hire your virtual assistant</span>
  </div>
</section>

<section class="started">
  <h2>Let's get started. It's about time to<br><b>supercharge your productivity!</b></h2>
  <p>Book a free consultation and we will match you with the right assistant for your business within days.</p>
  <span class="btn btn-blue">Request a consultation</span>
</section>

<footer>
  <div class="footer">
    <div class="fcol" style="left:240px"><h4>Paperlantern</h4>How it works<br>Pricing<br>Our team<br>FAQ</div>
    <div class="fcol" style="left:400px"><h4>Company</h4>About us<br>Careers<br>Blog</div>
    <div class="fcol" style="left:560px"><h4>Our Address</h4>Level 4, 88 Harbour Lane<br>Sydney NSW 2000<br>Australia</div>
    <div class="fcontact">
      <div><svg width="16" height="16" viewBox="0 0 24 24"><path d="M6 2h4l2 5-3 2a12 12 0 0 0 6 6l2-3 5 2v4a2 2 0 0 1-2 2A18 18 0 0 1 4 4a2 2 0 0 1 2-2z" fill="#33b8a4"/></svg>+61 2 5550 1842</div>
      <div><svg width="16" height="16" viewBox="0 0 24 24"><rect x="2" y="5" width="20" height="14" rx="2" fill="none" stroke="#33b8a4" stroke-width="2"/><path d="M2 6l10 7 10-7" fill="none" stroke="#33b8a4" stroke-width="2"/></svg>hello@paperlantern.com.au</div>
    </div>
  </div>
  <div class="touch">
    <h3>Get in touch</h3>
    <span class="contact"><svg width="16" height="16" viewBox="0 0 24 24"><path d="M2 12 22 3l-6 18-4-7z" fill="#fff"/></svg>Contact us</span>
    <div class="socials"><i style="background:#2f5a8f"></i><i style="background:#2aa3d8"></i><i style="background:#1a6fa0"></i><i style="background:#c9473a"></i></div>
  </div>
  <div class="legal">© 2015 Paperlantern.com.au. All rights reserved.</div>
</footer>

</body>
</html>
```